Lanternridge Partners Needs a Graphic Image

We need an image to use on our new website as well as on Chatterloop and Work Nest. The image should be 860x450 pixels and creatively use four colors: black, gold, gray, and white. The image design should focus on a "bank check." The amount of the check should be for $1 million. It should be made out to "Your Social-Purpose Organization." It should come from a hypothetical organization called The Meadowbright Trust with an address of 5870 Quillfern Court, Anywhere, USA. It should be signed by the CEO of The Meadowbright Trust. In the "comments area" of the check, it should read "Funding for Yr. 1 of Your Growth Capital Plan."

The organization and website you'll be creating this graphic for is called Lanternridge Partners LLC. We provide solutions that enable social purpose organizations to get the growth capital funding they need to turn their vision of the future into reality.

```html
<!DOCTYPE html>
<html lang="en">
<head>
<meta charset="utf-8">
<title>The Meadowbright Trust – Growth Capital Check</title>
<link rel="stylesheet" href="https://fonts.googleapis.com/css2?family=Caveat:wght@500&family=Italianno&family=Open+Sans:wght@400&family=Share+Tech+Mono&display=swap">
<style>
  :root {
    --paper: #ebe9e1;
    --paper-line: #e2e0d7;
    --gold: #c9b17e;
    --gold-dark: #9a7f48;
    --ink: #1c1c1c;
    --print: #2a2a2a;
    --rule: #4a4a4a;
    --white: #ffffff;
  }
  * { margin: 0; padding: 0; box-sizing: border-box; }
  html, body { width: 1200px; height: 628px; overflow: hidden; background: var(--paper); }
  .check {
    position: relative;
    width: 1200px;
    height: 628px;
    background: repeating-linear-gradient(to bottom, var(--paper) 0 3px, var(--paper-line) 3px 4px);
    font-family: "Open Sans", Arial, sans-serif;
    color: var(--print);
  }
  .frame { position: absolute; inset: 0; }
  .corner { position: absolute; width: 44px; height: 44px; background: var(--gold); border-radius: 50%; }
  .corner--tl { left: 6px; top: 6px; }
  .corner--tr { right: 6px; top: 6px; }
  .corner--bl { left: 6px; bottom: 6px; }
  .corner--br { right: 6px; bottom: 6px; }

  .issuer { position: absolute; left: 83px; top: 69px; font-size: 20px; line-height: 29px; font-style: normal; }
  .label { position: absolute; font-size: 16px; text-transform: uppercase; line-height: 24px; }
  .hand { position: absolute; font-family: "Caveat", "Comic Sans MS", cursive; font-weight: 500; color: var(--ink); white-space: nowrap; }
  .rule { position: absolute; height: 1px; background: var(--rule); }

  .date-label { left: 872px; top: 134px; }
  .date-rule { left: 872px; top: 159px; width: 212px; }

  .payee-label { left: 83px; top: 196px; }
  .payee { left: 248px; top: 187px; font-size: 38px; }
  .payee-rule { left: 180px; top: 250px; width: 628px; }
  .currency { left: 840px; top: 226px; font-size: 18px; }
  .amount-box { position: absolute; left: 870px; top: 196px; width: 214px; height: 54px; background: var(--white); }
  .amount { left: 893px; top: 200px; font-size: 34px; }

  .written-amount { left: 120px; top: 268px; font-size: 37px; }
  .written-line { position: absolute; left: 560px; top: 282px; }
  .written-rule { left: 83px; top: 323px; width: 1001px; }
  .dollars-label { left: 1002px; top: 299px; }

  .memo-label { left: 83px; top: 442px; }
  .memo { left: 160px; top: 416px; font-size: 38px; }
  .memo-rule { left: 83px; top: 466px; width: 697px; height: 2px; }
  .signature { position: absolute; left: 806px; top: 406px; font-family: "Italianno", "Brush Script MT", cursive; font-size: 49px; color: var(--ink); white-space: nowrap; }
  .signature-rule { left: 840px; top: 466px; width: 244px; }

  .micr { position: absolute; left: 83px; top: 518px; font-family: "Share Tech Mono", "Courier New", monospace; font-size: 26px; letter-spacing: 5.5px; color: var(--ink); white-space: pre; }
</style>
</head>
<body>
<main class="check">
  <svg class="frame" width="1200" height="628" viewBox="0 0 1200 628" role="img" aria-label="Gold ornamental check border">
    <rect x="12" y="12" width="1176" height="604" fill="none" stroke="var(--gold)" stroke-width="14"/>
    <rect x="4.5" y="4.5" width="1191" height="619" fill="none" stroke="var(--gold-dark)" stroke-width="1.5"/>
    <rect x="19.5" y="19.5" width="1161" height="589" fill="none" stroke="var(--gold-dark)" stroke-width="1.5"/>
  </svg>
  <div class="corner corner--tl" role="img" aria-label="Gold corner ornament"></div>
  <div class="corner corner--tr" role="img" aria-label="Gold corner ornament"></div>
  <div class="corner corner--bl" role="img" aria-label="Gold corner ornament"></div>
  <div class="corner corner--br" role="img" aria-label="Gold corner ornament"></div>

  <address class="issuer">
    The Meadowbright Trust<br>
    5870 Quillfern Court<br>
    Anywhere, USA
  </address>

  <div class="label date-label">Date</div>
  <div class="rule date-rule"></div>

  <div class="label payee-label">Pay to the<br>order of</div>
  <div class="hand payee">Your Social-Purpose Organization</div>
  <div class="rule payee-rule"></div>
  <div class="label currency">$</div>
  <div class="amount-box"></div>
  <div class="hand amount">1,000,000.00</div>

  <div class="hand written-amount">One million dollars and zero cents</div>
  <svg class="written-line" width="390" height="30" viewBox="0 0 390 30" aria-hidden="true">
    <path d="M2 16 C 60 12, 110 4, 150 8 S 200 22, 240 18 S 330 22, 385 22" fill="none" stroke="var(--ink)" stroke-width="2.2" stroke-linecap="round"/>
  </svg>
  <div class="rule written-rule"></div>
  <div class="label dollars-label">Dollars</div>

  <div class="label memo-label">Memo</div>
  <div class="hand memo">Funding for Yr. 1 of Your Growth Capital Plan</div>
  <div class="rule memo-rule"></div>
  <div class="signature">Dorian Halvey, CEO</div>
  <div class="rule signature-rule"></div>

  <div class="micr">:123456789: 1234   1234567890"</div>
</main>
</body>
</html>
```